Business Card Design Project- Removalist

I would like to surprise my husband to be with a different type of wedding present. His brother (who he owned a removalist business with) suddenly passed away from cancer recently and he has changed his business name to 'RTB' (which stands for Raising Tom Bright; but the full name doesn't need to be on the business card as it is more of a personal business name). To celebrate the new business I would like to get him some business cards made.
I would like the business name to be listed as 'RTB' and somewhere on the card I would like 'Sydney wide removals and relocation services'. I would like it to be obvious from the front of the card that it is a removalist business card. If a truck or some other feature that makes it look like a removalist business card could added it would be appreciated.
I don't mind what colours are used, but I would like the colour blue to feature somewhere in the design. It can be bright and fun, which is how Tom was.
I will also need the company's email address and phone number listed
The email address is: rtbremovals@quillpost.example
The contact number is: 0417 282 934
I don't need a contact name listed on the card, but perhaps 'Owned and operated by the Pendleworth family' could be added near the contact details in small font.
Thank you very much for considering this project!
Kind regards,
Fiona
Updates
Could you please change the mobile contact number to 0417 282 934. This is the only contact phone number required on the card now.
Thank you!

```html
<!DOCTYPE html>
<html lang="en">
<head>
<meta charset="utf-8">
<title>RTB Business Cards</title>
<link rel="stylesheet" href="https://fonts.googleapis.com/css2?family=Belleza&family=Tinos&display=swap">
<style>
  :root {
    --page: #ffffff;
    --navy: #14254f;
    --navy-deep: #0f1d40;
    --blue-light: #5aa8ec;
    --blue-mid: #2f7fd2;
    --blue-edge: #1f5fb4;
    --white: #ffffff;
  }
  * { margin: 0; padding: 0; box-sizing: border-box; }
  html, body {
    width: 898px;
    height: 1200px;
    overflow: hidden;
    background: var(--page);
  }
  .sheet {
    position: relative;
    width: 898px;
    height: 1200px;
  }
  .card {
    position: absolute;
    left: 90px;
    width: 718px;
    height: 402px;
    overflow: hidden;
  }

  /* Front */
  .card-front { top: 129px; background: var(--navy); }
  .front-texture {
    position: absolute;
    inset: 0;
    background: linear-gradient(135deg, var(--navy) 0%, var(--navy-deep) 100%);
  }
  .front-name {
    position: absolute;
    top: 68px;
    left: 0;
    width: 100%;
    text-align: center;
    font-family: "Belleza", sans-serif;
    font-size: 66px;
    letter-spacing: 6px;
    color: var(--white);
    line-height: 1;
  }
  .front-rule {
    position: absolute;
    top: 157px;
    left: 66px;
    width: 586px;
    height: 2px;
    background: var(--white);
  }
  .front-badge {
    position: absolute;
    left: 212px;
    top: 190px;
    width: 294px;
    height: 160px;
  }

  /* Back */
  .card-back {
    top: 549px;
    background: radial-gradient(ellipse 60% 70% at 50% 42%, var(--blue-light) 0%, var(--blue-mid) 55%, var(--blue-edge) 100%);
    color: var(--white);
    text-align: center;
  }
  .back-tagline {
    position: absolute;
    top: 32px;
    left: 0;
    width: 100%;
    font-family: "Belleza", sans-serif;
    font-size: 31px;
    line-height: 1;
  }
  .back-badge {
    position: absolute;
    left: 284px;
    top: 105px;
    width: 150px;
    height: 78px;
  }
  .back-name {
    position: absolute;
    top: 190px;
    left: 0;
    width: 100%;
    font-family: "Belleza", sans-serif;
    font-size: 64px;
    letter-spacing: 5px;
    color: var(--navy);
    line-height: 1;
  }
  .back-owner {
    position: absolute;
    top: 286px;
    left: 0;
    width: 100%;
    font-family: "Belleza", sans-serif;
    font-size: 25px;
    line-height: 1;
  }
  .back-contact {
    position: absolute;
    top: 322px;
    left: 0;
    width: 100%;
    font-family: "Tinos", serif;
    font-size: 21px;
    line-height: 33px;
  }
</style>
</head>
<body>
<main class="sheet">
  <section class="card card-front">
    <div class="front-texture" role="img" aria-label="Dark navy background with a faint repeating pattern"></div>
    <h1 class="front-name">RTB</h1>
    <div class="front-rule"></div>
    <svg class="front-badge" viewBox="0 0 294 160" aria-label="RTB">
      <ellipse cx="147" cy="80" rx="145" ry="78" fill="var(--navy)" stroke="var(--white)" stroke-width="3"/>
      <text x="147" y="98" text-anchor="middle" font-family="Belleza, sans-serif" font-size="50" fill="var(--white)">RTB</text>
    </svg>
  </section>

  <section class="card card-back">
    <p class="back-tagline">Sydney wide removals and relocation services</p>
    <svg class="back-badge" viewBox="0 0 150 78" aria-label="RTB">
      <ellipse cx="75" cy="39" rx="73" ry="37" fill="var(--navy)" stroke="var(--white)" stroke-width="2"/>
      <text x="75" y="48" text-anchor="middle" font-family="Belleza, sans-serif" font-size="26" fill="var(--white)">RTB</text>
    </svg>
    <h2 class="back-name">RTB</h2>
    <p class="back-owner">Owned and operated by the Pendleworth family</p>
    <p class="back-contact">rtbremovals@quillpost.example<br>0417 282 934</p>
  </section>
</main>
</body>
</html>
```